I need a business card design for a new dance business. I offer classical Indian dance tuition and also professional performances. I want to offer the community a variety of Indian dance experiences which include: group class and private tuition, school and preschool educational courses and workshops. dance theatre performances, community function workshops and performances, Kids Bollywood parties, wedding & conference performances, mouth percussion classes, Indian mythology/ dance costume and make up workshops.
The final design should communicate a feeling and impression of the vibrance and energy of Indian dance.
Updates
Hi Everyone,
Project Deadline Extended
Reason: I would like to refine a few changes to the details of this lovely design and we have run out of time!
Project Deadline Extended
Reason: Still waiting to hear back form designer re two possible changes to the card design. Tomorrow is the deadline and I have sent several messages but with no response. I need to see this through before selecting this lovely design.
Thank you.
Tara
Industry/Entity Type
Preschool
Requirements
Must have
- The front of the business card should have the photo of me (my face and torso), surrounded entirely by a border of bright magenta (to match the magenta of my lipstick - it is the same as the magenta on my skirt in the second photo). Within the top border I want (perhaps yellow-gold) writing to say "Tara Holloway - Artistic Director" and within the bottom border it should read "Silver Creek Kathak Studio." If you turn the card on its side the left border should have my telephone number: 0417 826 394 and the right-hand border should read: silvercreekkathakstudio@fernmail.example
The reverse of the card should be the orange of the dance costume
and I'd like the picture of my feet and legs to be on the right side of the back of the card as a side border. Centre-aligned on the orange background it should read (perhaps in dark magenta):
Indian dance classes + private tuition
School + preschool educational courses and workshops
Dance theatre performances
Community function workshops and performances
Children's Bollywood parties
Wedding + conference performances
Mouth percussion classes
Indian mythology and dance demonstration workshops
Dance costume and make-up workshops
Nice to have
- A lovely artistic but easy-to-read font would be nice.

```html
<!DOCTYPE html>
<html lang="en">
<head>
<meta charset="utf-8">
<title>Silver Creek Kathak Studio — Business Cards</title>
<link href="https://fonts.googleapis.com/css2?family=Oswald:wght@500;600&family=Roboto+Condensed:wght@700&display=swap" rel="stylesheet">
<style>
  :root {
    --magenta: #c8177f;
    --magenta-deep: #a3106a;
    --orange: #f28a12;
    --orange-light: #f7a52a;
    --gold: #ffe22e;
    --ink: #1c1c1c;
    --card-white: #f6f6f6;
    --card-grey: #e2e2e2;
    --page: #ffffff;
  }
  * { box-sizing: border-box; margin: 0; padding: 0; }
  html, body { width: 1200px; height: 589px; overflow: hidden; background: var(--page); }
  .sheet { position: relative; width: 1200px; height: 589px; }

  .card {
    position: absolute;
    container-type: inline-size;
    border-radius: 3.2% / 5.5%;
    overflow: hidden;
    box-shadow: 0 1px 3px rgba(0,0,0,.25);
  }
  .card--back-small  { left: 127px; top: 18px;  width: 424px; height: 204px; }
  .card--front-small { left: 733px; top: 18px;  width: 362px; height: 204px; }
  .card--front-large { left: 22px;  top: 255px; width: 573px; height: 327px; }
  .card--back-large  { left: 628px; top: 255px; width: 554px; height: 327px; }

  /* ---------- back of card ---------- */
  .back { background: var(--magenta); }
  .back__orange {
    position: absolute; left: 0; top: 13%; width: 72%; height: 76%;
    background: linear-gradient(180deg, var(--orange-light), var(--orange));
    clip-path: polygon(0 0, 100% 0, 92% 100%, 0 100%);
  }
  .back__photo {
    position: absolute; right: 0; top: 0; width: 42%; height: 100%;
    background: linear-gradient(160deg, #e9c7a8 0%, #d88a3a 35%, var(--orange) 60%, var(--magenta-deep) 100%);
    clip-path: polygon(18% 0, 100% 0, 100% 100%, 0 100%);
  }
  .back__title {
    position: absolute; left: 0; top: 26%; width: 68%; height: 9%;
    background: var(--ink);
    display: flex; align-items: center; padding-left: 4%;
    font-family: 'Roboto Condensed', sans-serif; font-weight: 700;
    color: var(--gold); font-size: 2.7cqw; text-transform: uppercase; letter-spacing: .02em;
  }
  .back__services {
    position: absolute; left: 4.5%; top: 41%; width: 62%;
    list-style: none;
    font-family: 'Roboto Condensed', sans-serif; font-weight: 700;
    color: #fff; font-size: 1.55cqw; line-height: 1.55; text-transform: uppercase;
  }
  .back__services li::before { content: "•"; margin-right: .6em; color: var(--gold); }

  /* ---------- front of card ---------- */
  .front {
    background: linear-gradient(135deg, var(--card-white) 0%, var(--card-grey) 55%, var(--card-white) 100%);
  }
  .front__bar {
    position: absolute; left: 0; width: 100%; background: var(--magenta);
    font-family: 'Oswald', sans-serif; font-weight: 600; color: var(--gold);
    text-transform: uppercase; display: flex; align-items: center;
  }
  .front__bar--top { top: 0; height: 18%; padding-left: 6%; font-size: 4.4cqw; letter-spacing: .03em; }
  .front__bar--top .role { font-size: .55em; margin-left: 1.4em; font-weight: 500; }
  .front__bar--bottom { bottom: 0; height: 15%; padding-left: 6%; font-size: 3.6cqw; letter-spacing: .02em; }
  .front__photo {
    position: absolute; right: 0; top: 0; width: 52%; height: 100%;
    background: linear-gradient(170deg, #7a3a2a 0%, #e6c3a3 30%, var(--orange) 62%, var(--magenta) 100%);
    clip-path: polygon(22% 0, 100% 0, 100% 100%, 8% 100%);
  }
  .front__contact {
    position: absolute; left: 6%; top: 69%; z-index: 1;
    font-family: 'Roboto Condensed', sans-serif; font-weight: 700;
    color: var(--ink); font-size: 2.05cqw; line-height: 1.45; text-transform: uppercase;
  }
</style>
</head>
<body>
<main class="sheet">

  <section class="card card--back-small back">
    <div class="back__orange"></div>
    <div class="back__photo" role="img" aria-label="Photograph of the dancer's feet and legs in orange costume"></div>
    <div class="back__title">Silver Creek Kathak Studio</div>
    <ul class="back__services">
      <li>Indian dance classes + private tuition</li>
      <li>School + preschool educational courses and workshops</li>
      <li>Dance theatre performances</li>
      <li>Community function workshops and performances</li>
      <li>Children's Bollywood parties</li>
      <li>Wedding + conference performances</li>
      <li>Mouth percussion classes</li>
      <li>Indian mythology and dance demonstration workshops</li>
      <li>Dance costume and make-up workshops</li>
    </ul>
  </section>

  <section class="card card--front-small front">
    <div class="front__photo" role="img" aria-label="Photograph of the artistic director in classical Indian dance pose"></div>
    <div class="front__bar front__bar--top">Tara Holloway<span class="role">(Artistic Director)</span></div>
    <p class="front__contact">Number: 0417 826 394<br>Email: silvercreekkathakstudio@fernmail.example</p>
    <div class="front__bar front__bar--bottom">Silver Creek Kathak Studio</div>
  </section>

  <section class="card card--front-large front">
    <div class="front__photo" role="img" aria-label="Photograph of the artistic director in classical Indian dance pose"></div>
    <div class="front__bar front__bar--top">Tara Holloway<span class="role">(Artistic Director)</span></div>
    <p class="front__contact">Number: 0417 826 394<br>Email: silvercreekkathakstudio@fernmail.example</p>
    <div class="front__bar front__bar--bottom">Silver Creek Kathak Studio</div>
  </section>

  <section class="card card--back-large back">
    <div class="back__orange"></div>
    <div class="back__photo" role="img" aria-label="Photograph of the dancer's feet and legs in orange costume"></div>
    <div class="back__title">Silver Creek Kathak Studio</div>
    <ul class="back__services">
      <li>Indian dance classes + private tuition</li>
      <li>School + preschool educational courses and workshops</li>
      <li>Dance theatre performances</li>
      <li>Community function workshops and performances</li>
      <li>Children's Bollywood parties</li>
      <li>Wedding + conference performances</li>
      <li>Mouth percussion classes</li>
      <li>Indian mythology and dance demonstration workshops</li>
      <li>Dance costume and make-up workshops</li>
    </ul>
  </section>

</main>
</body>
</html>
```